"Oral Surgery Office needs a Business Card Design with Logo"

We need a logo design and business card. The name of the office is Tassingford Oral Surgery & Implant Center. The final design should communicate uniqueness as well as highly class office. The business card should emphasize power. I included the current business card below. Please design something unique

Target Market(s)

Dentists & Patients

Industry/Entity Type

Dental

Contact Information for Business Card

Unique Design to show success, prestige, Style, unmatched performance

Font styles to use
Serif

Colors
1b1b1b
ffffff
0556a4

Requirements
Must have
• Bussiness Name, Doctor's Name, Website, phone and Fax, email, office address
• Color should be either Black and White or Blue and White
Nice to have
• Clean look
Should not have
• the business card shouldn't be too busy. I feel like the old business card was too busy

```html
<!DOCTYPE html>
<html lang="en">
<head>
<meta charset="utf-8">
<title>Tassingford Oral Surgery &amp; Implant Center – Business Card</title>
<link href="https://fonts.googleapis.com/css2?family=Open+Sans:wght@400;600;700&display=swap" rel="stylesheet">
<style>
  :root {
    --backdrop: #b5b5b5;
    --front-deep: #0b0b18;
    --front-glow: #24245a;
    --back-blue: #100a73;
    --ink: #ffffff;
    --ink-soft: #e8e8f0;
    --mark: #d9d9d4;
  }
  html, body {
    margin: 0; padding: 0;
    width: 1200px; height: 900px;
    overflow: hidden;
    background: var(--backdrop);
    font-family: "Open Sans", Arial, sans-serif;
    color: var(--ink);
  }
  .canvas { position: relative; width: 1200px; height: 900px; }

  .card { position: absolute; top: 275px; width: 477px; height: 294px; overflow: hidden; }
  .card--front {
    left: 116px;
    border-radius: 0 62px 0 62px;
    background: radial-gradient(ellipse 260px 150px at 250px 150px, var(--front-glow), var(--front-deep) 100%);
  }
  .card--back {
    left: 622px; top: 276px; height: 293px;
    border-radius: 62px 0 62px 0;
    background: var(--back-blue);
  }

  .brand { position: absolute; display: flex; align-items: center; }
  .brand__dot { border-radius: 50%; background: var(--mark); flex: none; }
  .brand__name {
    text-transform: uppercase; font-weight: 400; color: var(--ink);
    line-height: 1.08; text-align: center;
  }
  .card--front .brand { left: 42px; top: 32px; }
  .card--front .brand__dot { width: 62px; height: 62px; margin-right: 16px; }
  .card--front .brand__name { font-size: 19px; }
  .card--back .brand { left: 63px; top: 99px; }
  .card--back .brand__dot { width: 90px; height: 90px; margin-right: 22px; }
  .card--back .brand__name { font-size: 27px; }

  .doctor { position: absolute; right: 30px; top: 103px; text-align: right; }
  .doctor__name { font-weight: 700; font-size: 16px; margin: 0; }
  .doctor__title { font-size: 12.5px; margin: 4px 0 0; color: var(--ink-soft); }

  .divider { position: absolute; left: 0; right: 0; top: 153px; height: 1.5px; background: var(--ink-soft); }

  .contacts { position: absolute; right: 177px; top: 161px; margin: 0; padding: 0; list-style: none; }
  .contacts li {
    display: flex; justify-content: flex-end; align-items: center;
    font-size: 13px; height: 19.7px;
  }
  .contacts svg { width: 10px; height: 10px; margin-left: 7px; fill: var(--ink); }
  .address { position: absolute; right: 177px; top: 246px; font-size: 13px; margin: 0; }

  .social {
    position: absolute; left: 61px; top: 238px;
    display: flex; align-items: center; font-size: 13px; color: var(--ink-soft);
  }
  .social__item { display: flex; align-items: center; margin-right: 13px; }
  .social__square { width: 11px; height: 11px; border-radius: 2px; background: var(--ink-soft); margin-right: 6px; }
  .social__circle { width: 12px; height: 12px; border-radius: 50%; background: var(--ink-soft); margin-right: 6px; }
</style>
</head>
<body>
<main class="canvas">

  <section class="card card--front" aria-label="Business card front">
    <div class="brand">
      <span class="brand__dot"></span>
      <span class="brand__name">Tassingford<br>Oral Surgery &amp;<br>Implant Center</span>
    </div>

    <div class="doctor">
      <p class="doctor__name">Dr. Marlon Veskovic, D.D.S</p>
      <p class="doctor__title">Oral &amp; Maxillofacial Surgery</p>
    </div>

    <div class="divider"></div>

    <ul class="contacts">
      <li>555-014-4700
        <svg viewBox="0 0 10 10"><path d="M2 0.5 L3.6 2.6 L2.8 3.6 Q4 6 6.4 7.2 L7.4 6.4 L9.5 8 L8.4 9.5 Q3.5 9 0.5 1.6 Z"/></svg>
      </li>
      <li>555-014-5006
        <svg viewBox="0 0 10 10"><rect x="2.5" y="0.5" width="5" height="3"/><rect x="0.5" y="3.5" width="9" height="6" rx="1"/></svg>
      </li>
      <li>TassingfordSurgeon@mailbox.com
        <svg viewBox="0 0 10 10"><rect x="0.5" y="2" width="9" height="6.5"/><path d="M0.5 2 L5 5.8 L9.5 2" stroke="#0b0b18" stroke-width="1" fill="none"/></svg>
      </li>
      <li>www.TassingfordSurgeryCenter.com
        <svg viewBox="0 0 10 10"><circle cx="5" cy="5" r="4.6"/><path d="M0.5 5 H9.5 M5 0.5 V9.5" stroke="#0b0b18" stroke-width="0.8"/></svg>
      </li>
    </ul>

    <p class="address">2207 Harlow Avenue | Tassingford, NY 10990</p>
  </section>

  <section class="card card--back" aria-label="Business card back">
    <div class="brand">
      <span class="brand__dot"></span>
      <span class="brand__name">Tassingford<br>Oral Surgery &amp;<br>Implant Center</span>
    </div>

    <div class="social">
      <span class="social__item"><span class="social__square"></span>TassSurgeon</span>
      <span class="social__item"><span class="social__circle"></span>Tassingford Oral Surgery &amp; Implant Center</span>
    </div>
  </section>

</main>
</body>
</html>
```